Electrical business card

I require a business card for my company I will attach my log. My business is a electrical business. I would like the card to have a smart corporate look nothing to over the top.

Industry/Entity Type

Business

```html
<!DOCTYPE html>
<html lang="en">
<head>
<meta charset="utf-8">
<title>Voltline – Business Card</title>
<link href="https://fonts.googleapis.com/css2?family=Montserrat:wght@400;600;700&family=Open+Sans:wght@400;600&display=swap" rel="stylesheet">
<style>
  :root {
    --stage: #0b2340;
    --card-front: #e9e9e8;
    --card-back: #ffffff;
    --ink: #3a3a3a;
    --ink-soft: #5b5b5b;
    --brand-blue: #3bb6ec;
    --bar-dark: #3b3b3d;
  }
  * { margin: 0; padding: 0; box-sizing: border-box; }
  html, body { width: 674px; height: 1200px; overflow: hidden; }
  body { background: var(--stage); font-family: "Open Sans", Arial, sans-serif; position: relative; }

  .card { position: absolute; box-shadow: 0 10px 30px rgba(0,0,0,.35); }
  .card-front { left: 45px; top: 67px; width: 393px; height: 821px; background: var(--card-front); }
  .card-back  { left: 276px; top: 618px; width: 346px; height: 472px; background: var(--card-back); z-index: 2; }

  .brand { position: absolute; display: flex; flex-direction: column; align-items: flex-start; }
  .brand-name {
    font-family: "Montserrat", Arial, sans-serif; font-weight: 700; color: var(--ink);
    display: flex; align-items: center; gap: 8px; letter-spacing: 1px;
  }
  .brand-dot { border-radius: 50%; background: var(--brand-blue); display: inline-block; }
  .brand-tagline { font-family: "Montserrat", Arial, sans-serif; font-weight: 600; color: var(--brand-blue); letter-spacing: .5px; }

  .card-front .brand { left: 36px; top: 80px; }
  .card-front .brand-name { font-size: 34px; }
  .card-front .brand-dot { width: 14px; height: 14px; }
  .card-front .brand-tagline { font-size: 11px; margin-left: 2px; }

  .name-plate { position: absolute; left: 90px; top: 160px; width: 262px; }
  .name-bar {
    background: var(--bar-dark); color: #fff; height: 30px;
    font-family: "Montserrat", Arial, sans-serif; font-weight: 700; font-size: 19px;
    letter-spacing: 1px; padding-left: 16px; line-height: 30px; position: relative;
  }
  .name-bar::after { content: ""; position: absolute; right: 0; top: 0; width: 8px; height: 30px; background: var(--brand-blue); }
  .role-bar {
    height: 20px; border-bottom: 3px solid var(--brand-blue); padding-left: 16px;
    font-size: 10px; color: var(--ink); line-height: 18px; letter-spacing: .4px;
  }

  .contact-list { position: absolute; left: 28px; top: 278px; list-style: none; }
  .contact-list li { display: flex; align-items: flex-start; gap: 10px; font-size: 11.5px; color: var(--ink-soft); height: 31px; line-height: 17px; }
  .contact-list li.address { height: auto; }
  .contact-icon { width: 17px; height: 17px; flex: none; }

  .back-bands { position: absolute; left: 0; top: 0; }
  .card-back .brand { left: 0; right: 0; top: 134px; align-items: center; }
  .card-back .brand-name { font-size: 28px; }
  .card-back .brand-dot { width: 12px; height: 12px; }
  .card-back .brand-tagline { font-size: 9px; margin-left: 60px; }
</style>
</head>
<body>

<section class="card card-front">
  <div class="brand">
    <span class="brand-name"><span class="brand-dot"></span>VOLTLINE</span>
    <span class="brand-tagline">ELECTRICAL CONTRACTORS</span>
  </div>

  <div class="name-plate">
    <div class="name-bar">MARLO VENN</div>
    <div class="role-bar">ELECTRICAL CONTRACTOR</div>
  </div>

  <ul class="contact-list">
    <li>
      <svg class="contact-icon" viewBox="0 0 20 20"><circle cx="10" cy="10" r="9" fill="none" stroke="#8a8a8a" stroke-width="1.3"/><path d="M7 5.5l2 2-1 1.3a6 6 0 0 0 3.2 3.2l1.3-1 2 2-1.3 1.5C9.5 14 6 10.5 5.5 6.8z" fill="#8a8a8a"/></svg>
      <span>+61 400 555 019</span>
    </li>
    <li>
      <svg class="contact-icon" viewBox="0 0 20 20"><circle cx="10" cy="10" r="9" fill="none" stroke="#8a8a8a" stroke-width="1.3"/><rect x="5" y="6.5" width="10" height="7" fill="none" stroke="#8a8a8a" stroke-width="1.2"/><path d="M5 6.5l5 4 5-4" fill="none" stroke="#8a8a8a" stroke-width="1.2"/></svg>
      <span>marlo@voltline.example</span>
    </li>
    <li>
      <svg class="contact-icon" viewBox="0 0 20 20"><circle cx="10" cy="10" r="9" fill="none" stroke="#8a8a8a" stroke-width="1.3"/><circle cx="10" cy="10" r="5" fill="none" stroke="#8a8a8a" stroke-width="1.1"/><path d="M5 10h10M10 5c-2.5 3-2.5 7 0 10M10 5c2.5 3 2.5 7 0 10" fill="none" stroke="#8a8a8a" stroke-width="1"/></svg>
      <span>www.voltline.example</span>
    </li>
    <li>
      <svg class="contact-icon" viewBox="0 0 20 20"><circle cx="10" cy="10" r="9" fill="none" stroke="#8a8a8a" stroke-width="1.3"/><circle cx="10" cy="10" r="3" fill="#8a8a8a"/></svg>
      <span>@voltlineservices</span>
    </li>
    <li>
      <svg class="contact-icon" viewBox="0 0 20 20"><circle cx="10" cy="10" r="9" fill="none" stroke="#8a8a8a" stroke-width="1.3"/><rect x="7" y="7" width="6" height="6" fill="#8a8a8a"/></svg>
      <span>social: /voltlineservices</span>
    </li>
    <li class="address">
      <svg class="contact-icon" viewBox="0 0 20 20"><circle cx="10" cy="10" r="9" fill="none" stroke="#8a8a8a" stroke-width="1.3"/><path d="M10 15s-3.5-3.7-3.5-6.2a3.5 3.5 0 0 1 7 0C13.5 11.3 10 15 10 15z" fill="#8a8a8a"/><circle cx="10" cy="8.8" r="1.2" fill="#e9e9e8"/></svg>
      <span>88 Harbour Lane, Wattle Park,<br>Unit 5, Sydney,<br>Australia</span>
    </li>
  </ul>
</section>

<section class="card card-back">
  <svg class="back-bands" width="346" height="472" viewBox="0 0 346 472">
    <polygon points="0,118 250,52 346,52 346,118" fill="var(--brand-blue)"/>
    <polygon points="0,196 346,196 346,262 250,262" fill="var(--brand-blue)"/>
  </svg>
  <div class="brand">
    <span class="brand-name"><span class="brand-dot"></span>VOLTLINE</span>
    <span class="brand-tagline">ELECTRICAL CONTRACTORS</span>
  </div>
</section>

</body>
</html>
```